Dr Maren Holt, Orthopaedic Hand Surgeon

I am an orthopaedic hand surgeon and need business cards that reflect the surgery I do. I operate on bones, ligaments, tendons, and soft tissues. I can do microsurgery (surgery under an operating microscope) - including connecting ends of cut nerves and arteries in the fingers together. As an orthopaedic surgeon, I also fix fractures and manage orthopaedic trauma in the rest of the body. I favour black as a colour, and have some pictures of hand X-rays that you can use in the design, if you think that would look good (feel free to crop).

Hi all. Thank you for all your submissions so far. Please note that I have updated my project brief. I would like to emphasise that use of the logos that I have provided is optional, and if used, I would very much prefer the logo not to dominate the card, but add to the overall aesthetic of the card. Warm regards, Maren

Target Market(s)

Referring medical practitioners, hand therapists, patients

Industry/Entity Type

Healthcare

Contact Information for Business Card

Dr Maren Holt
Orthopaedic Hand Surgeon
MBBS BSc (Med), MIntPH (Merit), GWELN (Ortho), MIvroE

Font styles to use
Serif

Colors

Designer to choose colors to be used in the design.

Requirements
Must have
• Space for:
• 2 addresses (a PO Box Address and a consulting suite address) - to be confirmed
• 1 phone number - to be confirmed
Nice to have
• Please choose one of the GWELN logos (I included 3 - colour, black reverse, and greyscale); if you include this in the design, IT SHOULD NOT DOMINATE THE CARD, but be smaller and more discreet.
• I have also attached the MIvroE logo (colour and greyscale); if you choose to include this in the design, IT SHOULD NOT DOMINATE THE CARD, but be smaller and more discreet.
• I would love to be able to update details on the card as time goes on, and thus would like to own the template for the card as well.
• Also I would love discussion with regard to any changes on the card, if I am not completely happy with the design, and would like to discuss things such as ease of printing, finish on the cards (matte, polish) etc.
Should not have
• I don't like the card to look too crowded

```html
<!DOCTYPE html>
<html lang="en">
<head>
<meta charset="utf-8">
<title>Dr Maren Holt – Business Cards</title>
<link href="https://fonts.googleapis.com/css2?family=Spectral:wght@400;500;700&display=swap" rel="stylesheet">
<style>
  :root {
    --backdrop: #dcdddf;
    --card: #ffffff;
    --ink: #1d1d1d;
    --ink-soft: #333333;
    --xray-dark: #1b1b1b;
    --xray-light: #6e6e6e;
    --divider: #9a9a9a;
    --badge: #c9c9c9;
  }
  * { margin: 0; padding: 0; box-sizing: border-box; }
  html, body { width: 679px; height: 1200px; overflow: hidden; }
  body {
    background: var(--backdrop);
    font-family: "Spectral", Georgia, serif;
    color: var(--ink);
    position: relative;
  }
  .card {
    position: absolute;
    left: 76px;
    width: 526px;
    height: 322px;
    border-radius: 16px;
    background: var(--card);
    overflow: hidden;
    box-shadow: 0 2px 6px rgba(0,0,0,0.12);
  }
  .card--front { top: 76px; background: var(--xray-dark); }
  .card--back { top: 438px; }
  .card--back-alt { top: 801px; }

  .xray {
    position: absolute;
    top: 0; bottom: 0;
  }
  .xray--before {
    left: 0; width: 277px;
    background: radial-gradient(ellipse 45% 60% at 50% 55%, var(--xray-light), var(--xray-dark) 75%);
  }
  .xray--after {
    left: 249px; right: 0;
    background: radial-gradient(ellipse 40% 60% at 50% 50%, var(--xray-light), var(--xray-dark) 75%);
  }
  .divider { position: absolute; inset: 0; }
  .stage-label {
    position: absolute;
    left: 263px;
    transform: translate(-50%, -50%) rotate(90deg);
    color: #e6e6e6;
    font-size: 11.5px;
    letter-spacing: 1.2px;
    white-space: nowrap;
  }
  .stage-label--before { top: 121px; }
  .stage-label--after { top: 198px; }

  .frame { position: absolute; inset: 0; }
  .identity { position: absolute; left: 29px; }
  .identity__name {
    font-size: 20.5px;
    font-weight: 700;
    line-height: 1;
    white-space: nowrap;
  }
  .identity__role { font-size: 15px; font-weight: 700; }
  .identity__creds {
    font-size: 12.5px;
    color: var(--ink-soft);
    margin-top: 4px;
    white-space: nowrap;
  }
  .card--back .identity { top: 172px; }
  .card--back-alt .identity { top: 182px; }

  .contacts { position: absolute; list-style: none; font-size: 14.5px; line-height: 19.5px; }
  .contacts li { display: flex; align-items: center; gap: 6px; white-space: nowrap; }
  .contacts svg { width: 12px; height: 12px; fill: var(--ink); flex: none; }
  .card--back .contacts { left: 48px; top: 244px; }
  .card--back-alt .contacts { left: 30px; top: 244px; }

  .memberships {
    position: absolute;
    top: 40px; right: 29px;
    display: flex; gap: 22px; align-items: center;
  }
  .membership { display: flex; align-items: center; gap: 7px; font-size: 19px; color: #555; }
  .membership__mark { width: 34px; height: 42px; background: var(--badge); }
</style>
</head>
<body>

<section class="card card--front">
  <div class="xray xray--before" role="img" aria-label="Hand X-ray before surgery"></div>
  <div class="xray xray--after" role="img" aria-label="Hand X-ray after surgery"></div>
  <svg class="divider" width="526" height="322" viewBox="0 0 526 322">
    <path d="M277 0 V162 H249 V322" fill="none" stroke="var(--divider)" stroke-width="1.2"/>
  </svg>
  <span class="stage-label stage-label--before">BEFORE</span>
  <span class="stage-label stage-label--after">AFTER</span>
</section>

<section class="card card--back">
  <svg class="frame" width="526" height="322" viewBox="0 0 526 322">
    <path d="M495 0 V232 H30 V322" fill="none" stroke="var(--ink)" stroke-width="1.5"/>
  </svg>
  <div class="identity">
    <p class="identity__name">Dr. MAREN HOLT <span class="identity__role">/ Orthopaedic Hand Surgeon</span></p>
    <p class="identity__creds">MBBS BSc (Med), MIntPH (Merit), GWELN (Ortho), MIvroE</p>
  </div>
  <ul class="contacts">
    <li><svg viewBox="0 0 12 12"><path d="M0 2h12v8H0z M0 2l6 4.5L12 2" stroke="#fff" stroke-width="0.8"/></svg>PO Box 4821. Harlow Lane VIC 8011</li>
    <li><svg viewBox="0 0 12 12"><path d="M6 0a4 4 0 0 0-4 4c0 3 4 8 4 8s4-5 4-8a4 4 0 0 0-4-4zm0 5.6a1.6 1.6 0 1 1 0-3.2 1.6 1.6 0 0 1 0 3.2z"/></svg>57 Brennan St. Kelvale VIC 3000</li>
    <li><svg viewBox="0 0 12 12"><path d="M2.4 0.4l2 2.4-1.2 1.4c.8 1.8 2 3 3.8 3.8l1.4-1.2 2.4 2-1.2 2.6C4.6 11 1 7.4.4 2.2z"/></svg>+61 3 5550 1942</li>
  </ul>
</section>

<section class="card card--back-alt">
  <div class="memberships">
    <div class="membership"><span class="membership__mark"></span>GWELN</div>
    <div class="membership"><span class="membership__mark"></span>MIvroE</div>
  </div>
  <div class="identity">
    <p class="identity__name">Dr. MAREN HOLT <span class="identity__role">/ Orthopaedic Hand Surgeon</span></p>
    <p class="identity__creds">MBBS BSc (Med), MIntPH (Merit), GWELN (Ortho), MIvroE</p>
  </div>
  <svg class="frame" width="526" height="322" viewBox="0 0 526 322">
    <line x1="30" y1="232" x2="495" y2="232" stroke="var(--ink)" stroke-width="1.5"/>
  </svg>
  <ul class="contacts">
    <li><svg viewBox="0 0 12 12"><path d="M0 2h12v8H0z M0 2l6 4.5L12 2" stroke="#fff" stroke-width="0.8"/></svg>PO Box 4821. Harlow Lane VIC 8011</li>
    <li><svg viewBox="0 0 12 12"><path d="M6 0a4 4 0 0 0-4 4c0 3 4 8 4 8s4-5 4-8a4 4 0 0 0-4-4zm0 5.6a1.6 1.6 0 1 1 0-3.2 1.6 1.6 0 0 1 0 3.2z"/></svg>57 Brennan St. Kelvale VIC 3000</li>
    <li><svg viewBox="0 0 12 12"><path d="M2.4 0.4l2 2.4-1.2 1.4c.8 1.8 2 3 3.8 3.8l1.4-1.2 2.4 2-1.2 2.6C4.6 11 1 7.4.4 2.2z"/></svg>+61 3 5550 1942</li>
  </ul>
</section>

</body>
</html>
```